Improved Business Card, Government Contracting

We are looking to update the design of our business cards. We would like to create a template that can be used for future employees and easy to update.

Halvorsen Advisory Partners, LLC is a Service Disabled Veteran Owned Small Business with headquarters located in Leavenworth, KS. Our current website is www.hapteam.com. We have contracts in KS and VA with expansion opportunities in various other states. Our primary line of work is within government contracting and providing consulting services to various organizations within the Bureau of Frontier Works. We would like to project a professional image of our company that is consistent with the industry. Provided are previous versions of our business card template that shows our logo as well. We would like to make sure the information on the cards are easily noticeable .

Target Market(s)

Government Officials
Fellow Small Business Contractors
Large Business Contractors (ex. TRUX, Keswell Barnaby, Pryde Okonjo Whitcombe)

Industry/Entity Type

Business

Contact Information for Business Card

Dale Fenwick
Office Manager
Halvorsen Advisory Partners
Ph: 913.555.0172
Email: d.fenwick@hapteam.us
www.hapteam.com

Requirements
Must have
• The business mailing address is:
• 31842 204th Lane
• Leavenworth, KS 66099
Nice to have
• Embossed lettering

```html
<!DOCTYPE html>
<html lang="en">
<head>
<meta charset="utf-8">
<title>Halvorsen Advisory Partners – Business Card</title>
<link rel="stylesheet" href="https://fonts.googleapis.com/css2?family=Lato:wght@400;700;900&display=swap">
<style>
  :root {
    --backdrop: #e9e6e1;
    --brand-blue: #2e3192;
    --brand-yellow: #f8ec3c;
    --band-yellow: #fff462;
    --card-black: #050505;
    --text-white: #f2f2f2;
    --web-lilac: #d6d6f2;
  }
  * { margin: 0; padding: 0; box-sizing: border-box; }
  html, body { width: 1200px; height: 900px; overflow: hidden; }
  body {
    background: var(--backdrop);
    font-family: "Lato", sans-serif;
    position: relative;
  }
  .card {
    position: absolute;
    width: 640px;
    height: 366px;
    box-shadow: 0 10px 24px rgba(0,0,0,0.28);
    overflow: hidden;
  }
  /* Front */
  .card-front {
    left: 440px; top: 50px;
    background: var(--brand-blue);
  }
  .front-wordmark {
    position: absolute;
    left: 70px; top: 150px;
    display: flex; align-items: center; gap: 16px;
    color: var(--brand-yellow);
    font-weight: 900;
    font-size: 34px;
    letter-spacing: 0.2px;
  }
  .front-wordmark .mark-square {
    width: 26px; height: 26px;
    background: var(--brand-yellow);
  }
  .front-web {
    position: absolute;
    left: 72px; top: 262px;
    color: var(--web-lilac);
    font-size: 17px;
    letter-spacing: 14px;
  }
  /* Back */
  .card-back {
    left: 120px; top: 480px;
    background: var(--card-black);
  }
  .back-wordmark {
    position: absolute;
    left: 200px; top: 48px;
    color: var(--brand-yellow);
    font-weight: 700;
    font-size: 22px;
  }
  .contact-list {
    position: absolute;
    left: 34px; top: 150px;
    list-style: none;
    color: var(--text-white);
    font-size: 19px;
    line-height: 29px;
  }
  .contact-list li { display: flex; align-items: center; gap: 10px; }
  .contact-list svg { width: 16px; height: 16px; flex: none; }
  .holder {
    position: absolute;
    right: 34px; top: 160px;
    text-align: right;
  }
  .holder-name { color: var(--brand-yellow); font-weight: 700; font-size: 23px; }
  .holder-title { color: var(--text-white); font-size: 19px; }
  .address {
    position: absolute;
    right: 34px; top: 236px;
    text-align: right;
    font-size: 20px;
    line-height: 26px;
    color: var(--text-white);
  }
  .address .company { color: var(--brand-yellow); }
  .bottom-bands { position: absolute; left: 0; bottom: 0; width: 640px; height: 80px; }
</style>
</head>
<body>

<section class="card card-front" aria-label="Card front">
  <div class="front-wordmark"><span class="mark-square"></span>Halvorsen Advisory Partners</div>
  <div class="front-web">www.hapteam.com</div>
</section>

<section class="card card-back" aria-label="Card back">
  <div class="back-wordmark">Halvorsen Advisory Partners</div>

  <ul class="contact-list">
    <li>
      <svg viewBox="0 0 16 16" aria-hidden="true"><path fill="#f8ec3c" d="M2 9c0-4 12-4 12 0l-3 1-1-2H6L5 10 2 9zM4 10h8l1 4H3z"/></svg>
      913.555.0172
    </li>
    <li>
      <svg viewBox="0 0 16 16" aria-hidden="true"><rect x="1" y="3" width="14" height="10" fill="#f8ec3c"/><path d="M1 3l7 6 7-6" fill="none" stroke="#050505" stroke-width="1.4"/></svg>
      d.fenwick@hapteam.us
    </li>
    <li>
      <svg viewBox="0 0 16 16" aria-hidden="true"><g fill="none" stroke="#f8ec3c" stroke-width="1.4"><circle cx="8" cy="8" r="6.5"/><ellipse cx="8" cy="8" rx="3" ry="6.5"/><path d="M1.5 8h13M3 4.5h10M3 11.5h10"/></g></svg>
      www.hapteam.com
    </li>
  </ul>

  <div class="holder">
    <div class="holder-name">Dale Fenwick</div>
    <div class="holder-title">Office Manager</div>
  </div>

  <div class="address">
    <div class="company">Halvorsen Advisory Partners</div>
    <div>31842 204th Lane</div>
    <div>Leavenworth, KS 66099</div>
  </div>

  <svg class="bottom-bands" viewBox="0 0 640 80" aria-hidden="true">
    <polygon points="0,0 236,38 260,50 0,50" fill="#2e3192"/>
    <polygon points="0,16 0,80 640,80 640,58 262,52 236,44" fill="#fff462"/>
  </svg>
</section>

</body>
</html>
```